Business cards for Harbourline Supply Pty Ltd that import building products into Australia from China
Target Market(s)
Business to Business
Industry/Entity Type
Business
Contact Information for Business Card
Front: Logo and Business Name
Rear:
Vernon Ashcombe
General Manager
Mobile: 0427 619 354
email: vern@harbourlinesupply.com.au
alternative email: vern@coastwardgoods.com.au
web: www.harbourlinesupply.com.au
Adelaide, Brisbane and Darwin
Colors
ec1f27
fbee3d

```html
<!DOCTYPE html>
<html lang="en">
<head>
<meta charset="utf-8">
<title>Harbourline Supply Pty Ltd – Business Cards</title>
<link rel="stylesheet" href="https://fonts.googleapis.com/css2?family=Montserrat:wght@400;500;600;700&display=swap">
<style>
  :root {
    --backdrop: #2b2b2b;
    --card: #060606;
    --red: #ec1f27;
    --yellow: #fbee3d;
    --white: #ffffff;
    --rule: #8a8a8a;
  }
  * { margin: 0; padding: 0; box-sizing: border-box; }
  html, body { width: 1200px; height: 864px; overflow: hidden; }
  body {
    background: var(--backdrop);
    font-family: "Montserrat", sans-serif;
    color: var(--white);
    position: relative;
  }
  .card {
    position: absolute;
    width: 560px;
    height: 320px;
    background: var(--card);
    border-radius: 18px;
    box-shadow: 0 14px 30px rgba(0,0,0,0.55);
  }
  .card--front { left: 150px; top: 60px; }
  .card--back  { left: 490px; top: 484px; }

  /* Front */
  .brand {
    position: absolute;
    left: 0; right: 0; top: 118px;
    display: flex;
    justify-content: center;
    align-items: center;
    gap: 16px;
  }
  .brand__mark {
    width: 26px; height: 26px;
    background: var(--yellow);
  }
  .brand__name {
    color: var(--red);
    font-weight: 700;
    font-size: 30px;
    letter-spacing: 1.5px;
    line-height: 1.05;
    text-transform: uppercase;
  }
  .brand__name small {
    display: block;
    font-size: 15px;
    letter-spacing: 2.4px;
  }
  .locations {
    position: absolute;
    left: 0; right: 0; top: 236px;
    text-align: center;
    font-size: 14px;
    letter-spacing: 0.6px;
  }
  .locations .dot { color: var(--red); margin: 0 6px; }

  /* Back */
  .person {
    position: absolute;
    right: 300px; top: 120px;
    text-align: right;
  }
  .person__name { font-size: 30px; font-weight: 600; letter-spacing: 0.3px; }
  .person__role { font-size: 16px; color: var(--red); margin-top: 2px; letter-spacing: 0.4px; }
  .divider {
    position: absolute;
    left: 280px; top: 100px;
    width: 1px; height: 100px;
    background: var(--rule);
  }
  .contacts {
    position: absolute;
    left: 300px; top: 96px;
    list-style: none;
    font-size: 13px;
    letter-spacing: 0.2px;
  }
  .contacts li {
    display: flex;
    align-items: center;
    gap: 9px;
    height: 26px;
  }
  .contacts svg { width: 14px; height: 14px; flex: none; }
</style>
</head>
<body>
  <section class="card card--front" aria-label="Card front">
    <div class="brand">
      <span class="brand__mark"></span>
      <div class="brand__name">Harbourline Supply<small>Pty Ltd</small></div>
    </div>
    <p class="locations">Adelaide<span class="dot">•</span>Brisbane<span class="dot">•</span>Darwin</p>
  </section>

  <section class="card card--back" aria-label="Card back">
    <div class="person">
      <p class="person__name">Vernon Ashcombe</p>
      <p class="person__role">General Manager</p>
    </div>
    <span class="divider"></span>
    <ul class="contacts">
      <li>
        <svg viewBox="0 0 14 14" aria-hidden="true"><rect x="3.5" y="1" width="7" height="12" rx="1.2" fill="none" stroke="var(--yellow)" stroke-width="1.4"/><circle cx="7" cy="11" r="0.8" fill="var(--yellow)"/></svg>
        0427 619 354
      </li>
      <li>
        <svg viewBox="0 0 14 14" aria-hidden="true"><rect x="1" y="3" width="12" height="8" fill="var(--yellow)"/><path d="M1 3 L7 8 L13 3" fill="none" stroke="var(--card)" stroke-width="1.2"/></svg>
        vern@harbourlinesupply.com.au
      </li>
      <li>
        <svg viewBox="0 0 14 14" aria-hidden="true"><rect x="1" y="3" width="12" height="8" fill="var(--yellow)"/><path d="M1 3 L7 8 L13 3" fill="none" stroke="var(--card)" stroke-width="1.2"/></svg>
        vern@coastwardgoods.com.au
      </li>
      <li>
        <svg viewBox="0 0 14 14" aria-hidden="true"><g fill="none" stroke="var(--yellow)" stroke-width="1.1"><circle cx="7" cy="7" r="5.8"/><ellipse cx="7" cy="7" rx="2.6" ry="5.8"/><path d="M1.2 7 H12.8 M2 4 H12 M2 10 H12"/></g></svg>
        www.harbourlinesupply.com.au
      </li>
    </ul>
  </section>
</body>
</html>
```